Create a MAIN PAGE that is so enticing they won't say no. -Velm Kor website

High traffic site but we are not closing the deal as much as we should. Our retention rate is 90%. We believe that our site is not properly conveying to our clients the wonderous, exotic and unique experiences we provide them. Our site must give the same impression we give in person. We are seeking a designer to revise our main page & booking pages as these are our calling card pages.
Our industry is selling fantasy and escapism. We want our main page to convey two high class, discreet, sexy dominatrix's.
We want our booking page to be user friendly.
www.quorvelstudio.example

Target Market(s)

Adult Men ages 45-65

Industry/Entity Type

Sex

Coding

Coded - Design and coding required

Number of Pages Required

2 page

Font styles to use
Serif

Colors
EB3D1F
EC4F4E
F09395
F8D3D4
FCEDEE

Requirements
Must have
• Black & Red color theme, animation, clean, classy, sexy
Nice to have
• Smoke effect on the main page
Should not have
• Should not look basic

```html
<!DOCTYPE html>
<html lang="en">
<head>
<meta charset="utf-8">
<title>Velm Kor Atelier</title>
<link href="https://fonts.googleapis.com/css2?family=Cinzel:wght@400;600&family=Poppins:wght@400;500;600;700;800&display=swap" rel="stylesheet">
<style>
:root{
  --black:#050000;
  --ink:#0d0000;
  --red:#eb3d1f;
  --red-soft:#ec4f4e;
  --crimson:#c8101a;
  --pink:#f09395;
  --blush:#f8d3d4;
  --white:#ffffff;
  --muted:#e9dede;
}
*{margin:0;padding:0;box-sizing:border-box}
html,body{width:1200px;height:3028px;overflow:hidden;background:var(--black)}
body{position:relative;font-family:"Poppins",sans-serif;color:var(--white)}
.page{position:relative;width:1200px;height:3028px;overflow:hidden;
  background:
   radial-gradient(ellipse 260px 180px at 80px 300px,rgba(200,16,26,.55),transparent 70%),
   radial-gradient(ellipse 300px 200px at 1120px 120px,rgba(200,16,26,.5),transparent 70%),
   radial-gradient(ellipse 320px 220px at 1100px 620px,rgba(200,16,26,.45),transparent 70%),
   radial-gradient(ellipse 280px 260px at 60px 1500px,rgba(200,16,26,.55),transparent 70%),
   radial-gradient(ellipse 320px 260px at 1120px 1450px,rgba(200,16,26,.55),transparent 70%),
   radial-gradient(ellipse 500px 200px at 600px 1800px,rgba(200,16,26,.35),transparent 70%),
   radial-gradient(ellipse 320px 260px at 80px 2250px,rgba(200,16,26,.45),transparent 70%),
   radial-gradient(ellipse 320px 260px at 1130px 2300px,rgba(200,16,26,.45),transparent 70%),
   radial-gradient(ellipse 600px 240px at 600px 2900px,rgba(200,16,26,.35),transparent 70%),
   var(--black);}
.abs{position:absolute}
/* header */
.brand{left:44px;top:40px;font-family:"Cinzel",serif;font-size:21px;letter-spacing:1px;color:var(--red-soft)}
.nav{right:110px;top:42px;display:flex;gap:30px;font-size:15px;font-weight:500}
.cart{right:44px;top:34px;width:34px;height:34px;border-radius:50%;background:var(--red);display:flex;align-items:center;justify-content:center}
/* hero */
.hero-kicker{left:120px;top:260px;font-size:30px;font-weight:700;color:var(--red-soft)}
.hero-title{left:118px;top:300px;font-size:76px;line-height:82px;font-weight:800;letter-spacing:-1px}
.btn{background:var(--red);color:var(--white);border-radius:30px;font-weight:600;display:flex;align-items:center;justify-content:center}
.hero-btn{left:120px;top:505px;width:190px;height:60px;font-size:18px}
.hero-ring{left:560px;top:220px;width:380px;height:380px;border-radius:50%;
  background:radial-gradient(circle,#ff2a2a 0%,#d4111b 55%,#6e0008 100%);box-shadow:0 0 80px rgba(235,20,30,.7)}
.hero-photo{left:610px;top:70px;width:280px;height:670px;
  background:linear-gradient(180deg,#3a2a2a 0%,#1a1212 45%,#0b0606 100%);border-radius:120px 120px 0 0;opacity:.92}
/* section headings */
.kicker{left:0;width:1200px;text-align:center;font-size:15px;font-weight:700;color:var(--red)}
.heading{left:0;width:1200px;text-align:center;font-size:38px;font-weight:800}
.intro{left:195px;width:810px;text-align:center;font-size:14.5px;line-height:24px;color:var(--muted)}
/* package cards */
.card{top:990px;height:290px;overflow:hidden}
.card-photo{width:100%;height:100%}
.card-label{position:absolute;left:0;right:0;bottom:14px;text-align:center;font-size:20px;font-weight:700}
.card-feature{background:var(--red-soft);border:2px solid var(--blush);padding:34px 28px;text-align:center}
.card-feature h3{font-size:22px;font-weight:700;margin-bottom:10px}
.card-feature p{font-size:13px;line-height:20px;color:var(--blush)}
.card-feature span{display:block;margin-top:20px;font-size:13px;font-weight:600}
/* reviews */
.avatar{top:1418px;width:56px;height:56px;border-radius:50%;border:3px solid var(--white);background:linear-gradient(#8a5a4a,#3a2020)}
.quote{left:180px;width:840px;top:1520px;text-align:center;font-size:15px;line-height:25px;color:var(--muted)}
.reviewer{left:0;width:1200px;top:1636px;text-align:center;font-size:19px;font-weight:700}
.place{left:0;width:1200px;top:1666px;text-align:center;font-size:13px;color:var(--muted)}
.dots{left:568px;top:1712px;display:flex;gap:8px}
.dots i{width:9px;height:9px;border-radius:50%;background:var(--muted);opacity:.6}
.dots i:first-child{opacity:1;background:var(--white)}
/* specialties */
.tab-active{left:400px;top:2078px;width:190px;height:44px;font-size:14px}
.tab{left:620px;top:2090px;font-size:14px;font-weight:600}
.slide{border:6px solid var(--white);overflow:hidden}
.slide-center{left:430px;top:2160px;width:320px;height:460px;z-index:5}
.slide-caption{position:absolute;left:0;right:0;bottom:0;height:72px;background:var(--red);display:flex;align-items:center;justify-content:center;font-size:24px;font-weight:700}
.arrow{width:34px;height:34px;border-radius:50%;background:var(--red);display:flex;align-items:center;justify-content:center;z-index:8}
/* footer */
.foot-brand{left:0;width:1200px;top:2752px;text-align:center;font-family:"Cinzel",serif;font-size:28px;letter-spacing:1px;color:var(--red-soft)}
.foot-nav{left:0;width:1200px;top:2818px;display:flex;justify-content:center;gap:30px;font-size:15px;font-weight:500}
.copyright{left:0;width:1200px;top:2862px;text-align:center;font-size:14px}
.socials{left:0;width:1200px;top:2902px;display:flex;justify-content:center;gap:14px}
.socials i{width:28px;height:28px;border-radius:50%;background:var(--red)}
</style>
</head>
<body>
<div class="page">

  <header>
    <div class="abs brand">VELM KOR ATELIER</div>
    <nav class="abs nav"><span>Home</span><span>About</span><span>Gallery</span><span>Sessions</span><span>Book Sera &amp; Nyx</span><span>Links</span></nav>
    <div class="abs cart"><svg width="18" height="18" viewBox="0 0 18 18"><path d="M3 6h12l-1 10H4z" fill="none" stroke="#fff" stroke-width="1.8"/><path d="M6 6V4a3 3 0 0 1 6 0v2" fill="none" stroke="#fff" stroke-width="1.8"/></svg></div>
  </header>

  <section class="hero">
    <div class="abs hero-kicker">Welcome To</div>
    <h1 class="abs hero-title">Velm Kor<br>Atelier</h1>
    <div class="abs btn hero-btn">Get Started</div>
    <div class="abs hero-ring"></div>
    <div class="abs hero-photo" role="img" aria-label="Photo of the two hostesses standing together in dark evening outfits"></div>
  </section>

  <section class="packages">
    <div class="abs kicker" style="top:793px">Our menu</div>
    <h2 class="abs heading" style="top:812px">Package Sessions</h2>
    <p class="abs intro" style="top:862px">Our packages are just as unique as your experience with us will be. No need to worry that tiny train of yours trying to express what it is you are looking for exactly. You came to us because we know what you CRAVE and DESIRE. Raunchy roleplay &amp; titillating adventures await you. Want to add on a few extra naughty fetishes? Click HERE to browse our full Menu.</p>
    <div class="abs card" style="left:160px;width:300px">
      <div class="card-photo" role="img" aria-label="Photo for the light play session" style="background:linear-gradient(160deg,#2f6b3a,#5a3a2a 60%,#1a0e0a)"></div>
      <div class="card-label">Light BDSM Play</div>
    </div>
    <div class="abs card card-feature" style="left:468px;width:295px">
      <h3>Intro To Pegging</h3>
      <p>A slow, guided first session built around trust, clear limits and your comfort. Ask us about details.</p>
      <span>Learn More</span>
    </div>
    <div class="abs card" style="left:770px;width:270px">
      <div class="card-photo" role="img" aria-label="Photo for the training session" style="background:linear-gradient(160deg,#b59ab8,#6a5468 60%,#2a1e28)"></div>
      <div class="card-label">Slut Training</div>
    </div>
  </section>

  <section class="reviews">
    <div class="abs kicker" style="top:1350px">Our Reviews</div>
    <h2 class="abs heading" style="top:1368px">Client Reviews</h2>
    <div class="abs avatar" style="left:540px" role="img" aria-label="Client portrait"></div>
    <div class="abs avatar" style="left:572px;z-index:2;width:60px;height:60px;top:1416px" role="img" aria-label="Client portrait"></div>
    <div class="abs avatar" style="left:606px" role="img" aria-label="Client portrait"></div>
    <p class="abs quote">“ I highly recommend Goddess Nyx and Master Sera. Wow, one of the best experiences of my life. The communication was perfect leading up to the session. I had so many wow moments during the session, and couldn't believe how lucky I was to be there. This is definitely something that I will remember the rest of my life. I can't wait to see them again.”</p>
    <div class="abs reviewer">Dorian K</div>
    <div class="abs place">Marlow</div>
    <div class="abs dots"><i></i><i></i><i></i><i></i></div>
  </section>

  <section class="specialties">
    <div class="abs kicker" style="top:1990px">Interests</div>
    <h2 class="abs heading" style="top:2008px">Specialties</h2>
    <div class="abs btn tab-active">Specialties</div>
    <div class="abs tab">Limits / Please Do Not Ask</div>

    <div class="abs slide" style="left:165px;top:2220px;width:140px;height:360px" role="img" aria-label="Photo of a hostess in black"><div style="width:100%;height:100%;background:linear-gradient(#d9d2cc,#3a2a28)"></div></div>
    <div class="abs slide" style="left:290px;top:2195px;width:150px;height:405px;z-index:3" role="img" aria-label="Photo of a hostess in red"><div style="width:100%;height:100%;background:linear-gradient(#efe9e4,#8a2a2a 60%,#2a1a18)"></div></div>
    <div class="abs slide" style="left:740px;top:2195px;width:150px;height:405px;z-index:3" role="img" aria-label="Photo of a hostess outdoors"><div style="width:100%;height:100%;background:linear-gradient(#f4f0ea,#3a3030)"></div></div>
    <div class="abs slide" style="left:875px;top:2220px;width:140px;height:360px;z-index:2" role="img" aria-label="Photo of a session setting"><div style="width:100%;height:100%;background:linear-gradient(#6a8a5a,#3a2a26)"></div></div>
    <div class="abs slide" style="left:1000px;top:2245px;width:45px;height:310px" role="img" aria-label="Photo of a session setting"><div style="width:100%;height:100%;background:linear-gradient(#c2b6ae,#2a2020)"></div></div>

    <div class="abs slide slide-center" role="img" aria-label="Photo of the two hostesses posing for power play">
      <div style="width:100%;height:100%;background:linear-gradient(160deg,#2a7a4a,#e08aa8 55%,#6a3a48)"></div>
      <div class="slide-caption">Power Play</div>
    </div>

    <div class="abs arrow" style="left:150px;top:2372px"><svg width="12" height="12" viewBox="0 0 12 12"><path d="M8 1L3 6l5 5" fill="none" stroke="#fff" stroke-width="2"/></svg></div>
    <div class="abs arrow" style="left:1010px;top:2372px;background:#222"><svg width="12" height="12" viewBox="0 0 12 12"><path d="M4 1l5 5-5 5" fill="none" stroke="#fff" stroke-width="2"/></svg></div>
    <div class="abs" style="left:596px;top:2636px;width:9px;height:9px;border-radius:50%;background:#fff"></div>
  </section>

  <footer>
    <div class="abs foot-brand">VELM KOR ATELIER</div>
    <nav class="abs foot-nav"><span>Home</span><span>About</span><span>Gallery</span><span>Sessions</span><span>Book Sera &amp; Nyx</span><span>Links</span></nav>
    <div class="abs copyright">© copyrights 2022 Velm Kor Atelier &nbsp;|&nbsp; All rights reserved.</div>
    <div class="abs socials"><i></i><i></i><i></i><i></i></div>
  </footer>

</div>
</body>
</html>
```